buseisness card

design a card that similar to my web site
TRELLINGWORKSLLC .COM

Contact Information for Business Card

NAME PHONE # WEBSITE EMAIL AND DISCTIPTION OF WHAT WE DO

Colors
0054AA
0677BA
7BADD7
CADEEF
E8F1F8

Requirements
Must have
• lOGO AND DETAILS
Nice to have
• I LIKE THE WATER LIKE ON MY WEB SITE

```html
<!DOCTYPE html>
<html lang="en">
<head>
<meta charset="utf-8">
<title>Trelling Works – Business Card</title>
<link href="https://fonts.googleapis.com/css2?family=Montserrat:wght@400;500;700&display=swap" rel="stylesheet">
<style>
  :root{
    --deep-blue:#0054AA;
    --mid-blue:#0677BA;
    --sky-blue:#1f86bb;
    --soft-blue:#7BADD7;
    --pale-blue:#CADEEF;
    --mist:#E8F1F8;
    --ink:#1d1d1d;
    --white:#ffffff;
    --page:#e9ecef;
  }
  *{box-sizing:border-box;margin:0;padding:0}
  html,body{width:1200px;height:895px;overflow:hidden}
  body{background:var(--page);font-family:"Montserrat",Arial,sans-serif;position:relative}
  .card{position:absolute;width:720px;height:411px;left:240px;box-shadow:0 6px 18px rgba(0,0,0,.18);overflow:hidden}
  .card--front{top:22px;background:linear-gradient(30deg,var(--deep-blue) 0%,var(--mid-blue) 55%,var(--sky-blue) 100%);color:var(--white)}
  .card--back{top:462px;background:var(--white);color:var(--ink)}

  .brand{display:flex;align-items:center;gap:14px;font-weight:700;letter-spacing:1px;text-transform:uppercase}
  .brand__dot{width:30px;height:30px;border-radius:50%;flex:none}
  .card--front .brand{position:absolute;top:92px;left:0;right:0;justify-content:center;font-size:38px}
  .card--front .brand__dot{background:var(--white)}

  .features{position:absolute;left:40px;right:40px;bottom:52px;display:flex;justify-content:space-between;list-style:none}
  .feature{width:120px;text-align:center;font-size:13px;line-height:1.25;font-weight:400}
  .feature svg{display:block;margin:0 auto 8px;width:30px;height:30px;fill:none;stroke:var(--white);stroke-width:1.6;stroke-linecap:round;stroke-linejoin:round}

  .card--back .brand{position:absolute;left:44px;top:150px;font-size:30px;color:var(--mid-blue)}
  .card--back .brand__dot{background:var(--mid-blue)}
  .divider{position:absolute;left:392px;top:62px;width:1.5px;height:170px;background:var(--ink)}
  .contact{position:absolute;left:420px;top:60px}
  .contact__name{font-size:24px;font-weight:700;color:var(--mid-blue);text-transform:uppercase;letter-spacing:.3px}
  .contact__role{font-size:15px;margin-top:2px}
  .contact__list{list-style:none;margin-top:34px;font-size:14px;line-height:1.55}
  .contact__list li{display:flex;align-items:center;gap:10px}
  .contact__list svg{width:13px;height:13px;fill:var(--mid-blue);flex:none}
  .services{position:absolute;left:0;right:0;bottom:40px;height:40px;background:var(--mid-blue);color:var(--white);display:flex;align-items:center;justify-content:center;gap:14px;font-size:16px;font-weight:500}
</style>
</head>
<body>

<section class="card card--front">
  <div class="brand"><span class="brand__dot"></span><span>Trelling Works</span></div>
  <ul class="features">
    <li class="feature">
      <svg viewBox="0 0 30 30"><circle cx="15" cy="15" r="12"/><path d="M19 10.5c-1-1.2-2.4-1.6-4-1.6-2 0-3.5 1-3.5 2.6 0 3.5 7.5 2 7.5 5.8 0 1.7-1.6 2.8-4 2.8-1.7 0-3.2-.6-4-1.8M15 7v16"/></svg>
      Cost<br>Efficient
    </li>
    <li class="feature">
      <svg viewBox="0 0 30 30"><path d="M11 6l4-2 4 6M19 10l-3 1M8 13l-4 7 3 4h6M13 24l-2 2M22 15l4 6-3 4h-6M20 21l-3 3 3 1"/></svg>
      Environmentally<br>Friendly
    </li>
    <li class="feature">
      <svg viewBox="0 0 30 30"><path d="M10 4h10M12 4v19a3 3 0 006 0V4M12 14h6M14 18h2"/></svg>
      Thorough<br>Testing
    </li>
    <li class="feature">
      <svg viewBox="0 0 30 30"><path d="M4 12h22M4 22h22M8 7v13a2 2 0 004 0V7M14 7v13a2 2 0 004 0V7M20 7v13a2 2 0 004 0V7"/></svg>
      Variation<br>Testing
    </li>
    <li class="feature">
      <svg viewBox="0 0 30 30"><rect x="6" y="6" width="18" height="21" rx="1.5"/><path d="M11 4h8v4h-8zM10 13h10M10 17h10M10 21h7"/></svg>
      Requirement<br>Driven
    </li>
  </ul>
</section>

<section class="card card--back">
  <div class="brand"><span class="brand__dot"></span><span>Trelling Works</span></div>
  <div class="divider"></div>
  <div class="contact">
    <h1 class="contact__name">Dale Corwin</h1>
    <p class="contact__role">Founder and CEO</p>
    <ul class="contact__list">
      <li><svg viewBox="0 0 16 16"><path d="M3.5 1l2.5 3-1.5 1.5c.8 2 2.5 3.7 4.5 4.5L10.5 8.5l3 2.5-1.5 3C6.5 14 2 9.5 2 4z"/></svg>+740 555 0148</li>
      <li><svg viewBox="0 0 16 16"><path d="M1 3h14v10H1zM1.5 3.5L8 9l6.5-5.5" stroke="#fff" stroke-width="1"/></svg>info@trellingworksllc.com</li>
      <li><svg viewBox="0 0 16 16"><circle cx="8" cy="8" r="7"/><path d="M1 8h14M8 1c-3 4-3 10 0 14M8 1c3 4 3 10 0 14" stroke="#fff" stroke-width=".8" fill="none"/></svg>trellingworksllc.com</li>
    </ul>
  </div>
  <div class="services">
    <span>High Expansion Foam</span><span>|</span>
    <span>Alcohol Resistent Foam</span><span>|</span>
    <span>Aqueous Film Foaming</span>
  </div>
</section>

</body>
</html>
```